I need a design for Corvane Homes which is a custom home builder. The name on it will be Dan Hartley, and I will give the phone number to the winning design. No address or website needed.

```html
<!DOCTYPE html>
<html lang="en">
<head>
<meta charset="utf-8">
<title>Corvane Homes – Business Card</title>
<link rel="stylesheet" href="https://fonts.googleapis.com/css2?family=Open+Sans:wght@400;600&family=Gelasio:wght@400&display=swap">
<style>
  :root {
    --stage: #e9e6e1;
    --card-dark: #141414;
    --card-dark-edge: #262626;
    --card-light: #ffffff;
    --ink: #1c1c1c;
    --gold: #c9a12c;
    --gold-deep: #b88f1f;
    --on-dark: #f4f4f4;
  }
  * { box-sizing: border-box; margin: 0; padding: 0; }
  html, body {
    width: 1200px; height: 1023px; overflow: hidden;
    background: var(--stage);
  }
  .stage {
    position: relative; width: 1200px; height: 1023px;
  }
  .card {
    position: absolute; left: 240px; width: 720px; height: 411px;
    border-radius: 4px;
    box-shadow: 0 6px 18px rgba(0,0,0,.18);
    overflow: hidden;
  }
  /* Back side */
  .card--back {
    top: 60px;
    background: radial-gradient(ellipse at 50% 45%, var(--card-dark-edge) 0%, var(--card-dark) 70%);
    display: flex; flex-direction: column; align-items: center; justify-content: center;
    color: var(--on-dark);
    font-family: "Open Sans", sans-serif;
  }
  .card--back .wordmark {
    font-weight: 600; font-size: 50px; letter-spacing: 2px; line-height: 1;
  }
  .card--back .tagline {
    font-weight: 400; font-size: 30px; letter-spacing: .5px; margin-top: 8px;
  }
  /* Front side */
  .card--front {
    top: 552px;
    background: var(--card-light);
    font-family: "Open Sans", sans-serif;
  }
  .front-logo {
    position: absolute; left: 52px; top: 78px;
  }
  .front-logo .wordmark {
    font-weight: 600; font-size: 50px; letter-spacing: 2px; line-height: 1;
    color: var(--ink);
  }
  .front-logo .tagline {
    font-weight: 400; font-size: 30px; color: var(--gold); margin-top: 8px; letter-spacing: .3px;
  }
  .person {
    position: absolute; left: 60px; top: 230px;
    font-family: "Gelasio", serif;
  }
  .person .name { font-size: 31px; color: var(--ink); line-height: 1.1; }
  .person .role { font-size: 22px; color: var(--gold); margin-top: 2px; }
  .contact {
    position: absolute; right: 62px; top: 310px;
    list-style: none;
    font-family: "Gelasio", serif; font-size: 20px; color: var(--ink);
  }
  .contact li { display: flex; align-items: center; gap: 12px; height: 32px; }
  .contact svg { width: 16px; height: 16px; flex: none; }
  .accent-band {
    position: absolute; left: 0; right: 0; bottom: 0; height: 12px;
    background: linear-gradient(90deg, var(--gold-deep), var(--gold), var(--gold-deep));
  }
</style>
</head>
<body>
<main class="stage">
  <section class="card card--back" aria-label="Card back">
    <div class="wordmark">CORVANE HOMES</div>
    <div class="tagline">CUSTOM HOME BUILDER</div>
  </section>

  <section class="card card--front" aria-label="Card front">
    <div class="front-logo">
      <div class="wordmark">CORVANE HOMES</div>
      <div class="tagline">CUSTOM HOME BUILDER</div>
    </div>
    <div class="person">
      <div class="name">Dan Hartley</div>
      <div class="role">Civil Engineer</div>
    </div>
    <ul class="contact">
      <li>
        <svg viewBox="0 0 16 16" aria-hidden="true"><rect x="4" y="1" width="8" height="14" rx="1.5" fill="none" stroke="#c9a12c" stroke-width="1.4"/><circle cx="8" cy="12.5" r=".9" fill="#c9a12c"/></svg>
        <span>555-014-2290</span>
      </li>
      <li>
        <svg viewBox="0 0 16 16" aria-hidden="true"><rect x="1" y="3.5" width="14" height="9" fill="#c9a12c"/><path d="M1 3.5 L8 9 L15 3.5" fill="none" stroke="#fff" stroke-width="1.2"/></svg>
        <span>your@mailbox.com</span>
      </li>
    </ul>
    <div class="accent-band"></div>
  </section>
</main>
</body>
</html>
```